We are looking for a new stationary design for all templates, business cards, letterheads, envelopes, pads, stamps and accessories. It needs to be unique, slick, and ooze premium quality. The details to go on the stationary are as follows:
Name: The Larnmore Dental Clnic, Dentist: Dr. Declan Brophy BDS NUI (hons), Dr. Aisling Dunphy BScDent BA (separate card per dentist) tel: 0407 58213 add: The Larnmore Dental Clinic, Meadowbank Care Campus, Ballyfarnagh, Wicklow Town, County Wicklow. web: www.thelarnmoredentalclinic.example email: info@thelarnmoredentalclinic.example
Colour pallet is: primary blue, white, secondary black and grey.
We have attached all source files for the logo below. We want a textured card, with embossed, icons and name on front, no need to repeat it o the reverse. True blue would be the dominant colour.
Besides this let your imagination go wild.
Thank you. TLDC.

```html
<!DOCTYPE html>
<html lang="en">
<head>
<meta charset="utf-8">
<title>The Larnmore Dental Clinic – Stationery</title>
<link rel="stylesheet" href="https://fonts.googleapis.com/css2?family=Questrial&family=Arimo:wght@400;700&display=swap">
<style>
:root{
  --bg:#eceeef;
  --paper:#ffffff;
  --charcoal:#555557;
  --charcoal-dark:#333335;
  --blue:#1f84c8;
  --blue-light:#4aa6e0;
  --ink:#4a4a4c;
  --muted:#8a8a8c;
  --silver-1:#e4e4e4;
  --silver-2:#fbfbfb;
}
*{margin:0;padding:0;box-sizing:border-box}
html,body{width:1200px;height:937px;overflow:hidden;background:var(--bg)}
body{position:relative;font-family:"Arimo",Arial,sans-serif;color:var(--ink)}
.piece{position:absolute;background:var(--paper);box-shadow:0 2px 6px rgba(0,0,0,.12)}
.brand{display:flex;align-items:center;font-family:"Questrial",sans-serif;color:var(--ink);white-space:nowrap}
.brand .mark{background:var(--blue);border-radius:3px;flex:none}

/* letterhead */
.letterhead{left:185px;top:66px;width:385px;height:546px}
.letterhead .brand{position:absolute;left:17px;top:22px;font-size:11px}
.letterhead .brand .mark{width:16px;height:16px;margin-right:6px}
.letter{position:absolute;left:36px;top:140px;width:290px;font-size:5.2px;line-height:7.4px;color:#555}
.letter p{margin-bottom:9px}
.letter .gap{margin-bottom:22px}
.letter b{color:#333}
.signature{width:40px;height:22px;background:linear-gradient(90deg,#d9d9d9,#efefef);margin:4px 0 6px}
.letter-foot{position:absolute;left:0;right:0;bottom:18px;height:24px;background:var(--charcoal);border-top:2px solid var(--blue);display:flex;align-items:center;justify-content:center;gap:22px;color:#eee;font-size:4.4px;line-height:6px}
.foot-item{display:flex;align-items:center;gap:5px;white-space:nowrap}
.foot-item svg{width:12px;height:12px;flex:none}

/* folder */
.folder{left:636px;top:41px;width:458px;height:575px;background:var(--charcoal)}
.folder-band{position:absolute;left:0;right:0;top:203px;height:166px;background:linear-gradient(180deg,var(--silver-1),var(--silver-2) 50%,var(--silver-1));border-top:4px solid var(--charcoal-dark);border-bottom:4px solid var(--charcoal-dark);display:flex;align-items:center;justify-content:center}
.folder-band .brand{font-size:22px;letter-spacing:.5px}
.folder-band .brand .mark{width:38px;height:38px;margin-right:12px;border-radius:5px}
.folder-url{position:absolute;left:0;right:0;bottom:14px;text-align:center;color:#fff;font-family:"Questrial",sans-serif;font-size:12px;letter-spacing:2px}

/* business cards */
.card{width:177px;height:97px;overflow:hidden}
.card-front{left:45px;top:658px}
.card-back{left:45px;top:785px;display:flex;align-items:center;justify-content:center}
.card-front .brand{position:absolute;left:0;right:0;top:8px;justify-content:center;font-size:7.5px}
.card-front .brand .mark{width:10px;height:10px;margin-right:4px;border-radius:2px}
.card-band{position:absolute;left:0;right:0;top:27px;height:44px;background:var(--charcoal);color:#eee;font-size:3.6px;line-height:5px}
.card-band .icon{position:absolute;top:6px;width:11px;height:11px}
.card-band .name{position:absolute;left:7px;top:22px;font-family:"Questrial",sans-serif;font-size:5.6px;line-height:7px;color:#fff;white-space:nowrap}
.card-band .role{position:absolute;left:7px;top:30px;white-space:nowrap}
.card-band .web{position:absolute;left:72px;top:24px;white-space:nowrap}
.card-band .tel{position:absolute;left:146px;top:24px;white-space:nowrap}
.card-follow{position:absolute;left:8px;top:75px;font-size:4.6px;line-height:5px;color:#555}
.card-follow small{display:block;font-size:3.4px;color:var(--muted)}
.social{position:absolute;left:56px;top:76px;display:flex;gap:4px}
.social span{width:6px;height:6px;background:var(--blue)}
.card-back .brand{font-size:9px}
.card-back .brand .mark{width:16px;height:16px;margin-right:5px}

/* envelope front */
.envelope{left:265px;top:671px;width:432px;height:209px}
.envelope .brand{position:absolute;left:14px;top:20px;font-size:11px}
.envelope .brand .mark{width:20px;height:20px;margin-right:7px}
.envelope .return{position:absolute;left:14px;top:50px;font-size:5.4px;color:#555}
.envelope-band{position:absolute;left:0;right:0;top:166px;height:23px;background:var(--charcoal);color:#fff;display:flex;align-items:center;justify-content:center;font-family:"Questrial",sans-serif;font-size:10px;letter-spacing:2px}

/* envelope back */
.envelope-back{left:737px;top:671px;width:431px;height:209px;overflow:hidden}
.flap{position:absolute;left:0;right:0;top:0;height:72px;background:var(--charcoal);border-radius:0 0 52px 52px/0 0 42px 42px;display:flex;align-items:center;justify-content:center;color:#fff;font-family:"Questrial",sans-serif;font-size:12px;letter-spacing:2px}
</style>
</head>
<body>

<section class="piece letterhead">
  <div class="brand"><span class="mark"></span>The Larnmore Dental Clinic</div>
  <div class="letter">
    <p>July 2, 2012</p>
    <p><b>Dear Cli,</b><br>Harbour House, Quay St., Ireland</p>
    <p class="gap">Thank you for choosing our clinic for your dental care. This letter confirms the details of your upcoming visit and outlines what you can expect on the day. Please arrive ten minutes early so our team can update your records and answer any questions you may have before your appointment begins.</p>
    <p class="gap">If you need to change the time, simply call the clinic and our reception staff will gladly find a new slot that suits you.</p>
    <p>We look forward to welcoming you. Our aim is to make every visit calm, clear and comfortable, from the first check-up to any follow-up treatment. Should you have concerns about cost, comfort or timing, please let us know in advance so we can plan your care together and keep you fully informed at every step.</p>
    <p>Best Regards,</p>
    <div class="signature" role="img" aria-label="Handwritten signature"></div>
    <p><b>Dr. Declan Brophy</b><br>BDS NUI (hons)<br><br>Meadowbank Care Campus, Ballyfarnagh, Wicklow Town</p>
  </div>
  <div class="letter-foot">
    <div class="foot-item">
      <svg viewBox="0 0 12 12"><circle cx="6" cy="6" r="6" fill="#1f84c8"/><path d="M6 2.5a2 2 0 0 0-2 2c0 1.6 2 4 2 4s2-2.4 2-4a2 2 0 0 0-2-2z" fill="#fff"/></svg>
      <span>Meadowbank Care Campus,<br>Ballyfarnagh, Wicklow Town</span>
    </div>
    <div class="foot-item">
      <svg viewBox="0 0 12 12"><circle cx="6" cy="6" r="6" fill="#1f84c8"/><rect x="4" y="2.5" width="4" height="7" rx=".8" fill="#fff"/></svg>
      <span>Tel: 0407 58213<br>County Wicklow</span>
    </div>
    <div class="foot-item">
      <svg viewBox="0 0 12 12"><circle cx="6" cy="6" r="6" fill="#1f84c8"/><circle cx="6" cy="6" r="3.3" fill="none" stroke="#fff" stroke-width=".7"/><path d="M2.7 6h6.6M6 2.7v6.6" stroke="#fff" stroke-width=".6"/></svg>
      <span>info@thelarnmoredentalclinic.example<br>www.thelarnmoredentalclinic.example</span>
    </div>
  </div>
</section>

<section class="piece folder">
  <div class="folder-band">
    <div class="brand"><span class="mark"></span>The Larnmore Dental Clinic</div>
  </div>
  <div class="folder-url">www.thelarnmoredentalclinic.example</div>
</section>

<section class="piece card card-front">
  <div class="brand"><span class="mark"></span>The Larnmore Dental Clinic</div>
  <div class="card-band">
    <svg class="icon" style="left:24px" viewBox="0 0 12 12"><circle cx="6" cy="6" r="6" fill="#1f84c8"/><circle cx="6" cy="4.6" r="1.6" fill="#fff"/><path d="M3.3 9a2.7 2.4 0 0 1 5.4 0z" fill="#fff"/></svg>
    <svg class="icon" style="left:100px" viewBox="0 0 12 12"><circle cx="6" cy="6" r="6" fill="#1f84c8"/><circle cx="6" cy="6" r="3.3" fill="none" stroke="#fff" stroke-width=".7"/><path d="M2.7 6h6.6M6 2.7v6.6" stroke="#fff" stroke-width=".6"/></svg>
    <svg class="icon" style="left:151px" viewBox="0 0 12 12"><circle cx="6" cy="6" r="6" fill="#1f84c8"/><rect x="4" y="2.5" width="4" height="7" rx=".8" fill="#fff"/></svg>
    <div class="name">DR. DECLAN BROPHY</div>
    <div class="role">BDS NUI (hons)</div>
    <div class="web">info@thelarnmoredentalclinic.example<br>www.thelarnmoredentalclinic.example</div>
    <div class="tel">0407 58213<br>Wicklow</div>
  </div>
  <div class="card-follow">FOLLOW US<small>on social networks</small></div>
  <div class="social"><span></span><span></span><span></span><span></span></div>
</section>

<section class="piece card card-back">
  <div class="brand"><span class="mark"></span>The Larnmore Dental Clinic</div>
</section>

<section class="piece envelope">
  <div class="brand"><span class="mark"></span>The Larnmore Dental Clinic</div>
  <div class="return">Meadowbank Care Campus, Ballyfarnagh, Wicklow Town, County Wicklow</div>
  <div class="envelope-band">www.thelarnmoredentalclinic.example</div>
</section>

<section class="piece envelope-back">
  <div class="flap">www.thelarnmoredentalclinic.example</div>
</section>

</body>
</html>
```